web and logo design for insurance quote site

i want a quoteform site simimar to brimtallow.com i have a site up now @ kvbrimtallow.com, its functional but not attractive

Target Market(s)

people looking to get a home, auto or life insurance quote

Industry/Entity Type

Insurance

Number of Pages Required

1 page

Requirements
Must have
• great form that gathers all the information and emails the form to me
Nice to have
• nice eye catching art design thatI can have printed on business cards to send poeople to the site

```html
<!DOCTYPE html>
<html lang="en">
<head>
<meta charset="utf-8">
<title>KVBrimtallow – Insurance Quotes</title>
<link href="https://fonts.googleapis.com/css2?family=Nunito+Sans:wght@400;600;700;800;900&display=swap" rel="stylesheet">
<style>
  :root {
    --brand-blue: #2aa6d6;
    --band-blue: #1a93c0;
    --band-light: #b7deee;
    --ink: #111111;
    --muted: #444444;
    --rule: #c9c9c9;
    --panel-border: #bdbdbd;
    --life-blue: #1f5fa8;
    --car-orange: #d2541c;
    --home-green: #3e9a3a;
    --biz-blue: #1f5fa8;
    --tab-bg: #f4f4f4;
    --page: #ffffff;
  }
  * { box-sizing: border-box; margin: 0; padding: 0; }
  html, body { width: 1200px; height: 841px; overflow: hidden; background: var(--page); }
  body { position: relative; font-family: "Nunito Sans", Arial, sans-serif; color: var(--ink); }
  .abs { position: absolute; }

  .side-band { position: absolute; top: 22px; width: 38px; height: 796px;
    background: linear-gradient(to bottom, var(--band-blue) 0%, var(--band-blue) 55%, var(--band-light) 100%); }
  .side-band.left { left: 12px; }
  .side-band.right { left: 866px; width: 34px; }

  .wordmark { font-weight: 900; color: var(--ink); letter-spacing: -0.5px; display: flex; align-items: center; gap: 8px; white-space: nowrap; }
  .wordmark .mark-square { display: inline-block; background: var(--brand-blue); flex: none; }
  .site-logo { left: 98px; top: 60px; font-size: 29px; }
  .site-logo .mark-square { width: 26px; height: 26px; }

  .care { left: 570px; top: 48px; font-size: 18px; font-weight: 700; white-space: nowrap; }
  .care span { color: var(--brand-blue); }
  .util-links { left: 594px; top: 76px; font-size: 18px; font-weight: 700; display: flex; gap: 24px; }
  .util-links li { list-style: none; }
  .util-links li::before { content: "\25B6"; font-size: 10px; margin-right: 3px; vertical-align: 2px; }

  .main-nav { left: 103px; top: 146px; display: flex; gap: 2px; }
  .main-nav li { list-style: none; width: 141px; height: 30px; border: 1px solid var(--panel-border); border-bottom: none;
    border-radius: 8px 8px 0 0; background: linear-gradient(#ffffff, var(--tab-bg)); text-align: center;
    font-size: 15px; font-weight: 600; line-height: 30px; white-space: nowrap; overflow: hidden; }
  .main-nav li.active { color: var(--brand-blue); }
  .nav-rule { left: 86px; top: 176px; width: 746px; height: 5px; border-top: 2px solid var(--rule); border-bottom: 1px solid var(--rule); }

  .hero { top: 190px; width: 244px; height: 160px; border: 1px solid var(--panel-border); overflow: hidden; }
  .hero .photo { position: absolute; inset: 0; }
  .hero.life { left: 86px; } .hero.life .photo { background: linear-gradient(90deg, #c9d2dc 0%, #7f9cc2 45%, var(--life-blue) 100%); }
  .hero.car { left: 338px; } .hero.car .photo { background: linear-gradient(90deg, #eef1f3 0%, #c7cdd2 40%, var(--car-orange) 75%); }
  .hero.home { left: 588px; } .hero.home .photo { background: linear-gradient(90deg, #e8e3cf 0%, #b7c99a 45%, var(--home-green) 100%); }
  .hero h2 { position: absolute; right: 10px; top: 12px; color: #fff; font-size: 30px; font-weight: 700; line-height: 26px; text-align: right; }
  .hero h2 small { display: block; font-size: 15px; font-weight: 700; line-height: 20px; }
  .hero .cta { position: absolute; right: 0; bottom: 0; width: 88px; height: 38px; background: #fff; border-top-left-radius: 8px;
    text-align: center; font-size: 15px; font-weight: 600; line-height: 15px; padding-top: 4px; }

  .panel { border: 1px solid var(--panel-border); background: #fff; }
  .welcome { left: 86px; top: 365px; width: 494px; height: 225px; }
  .welcome .portrait { position: absolute; left: 28px; top: 2px; width: 80px; height: 220px;
    background: linear-gradient(to bottom, #e6e6e6, #9b9b9b 40%, #3a3a3a 85%, #e6e6e6); border-radius: 30px 30px 4px 4px; }
  .welcome h1 { position: absolute; left: 110px; top: 18px; font-size: 22px; font-weight: 700; color: var(--brand-blue); white-space: nowrap; }
  .welcome p { position: absolute; left: 110px; top: 48px; width: 380px; font-size: 16px; font-weight: 600; line-height: 29px; white-space: nowrap; }

  .quote-box { left: 588px; top: 365px; width: 244px; height: 225px; }
  .quote-box h2 { text-align: center; color: var(--brand-blue); font-size: 22px; font-weight: 600; line-height: 28px; margin-top: 5px; }
  .quote-box label { position: absolute; font-size: 13px; text-align: right; line-height: 14px; }
  .quote-box .field { position: absolute; left: 71px; width: 164px; height: 20px; border: 1px solid var(--panel-border); background: #fafafa; font-size: 14px; padding-left: 6px; line-height: 18px; }
  .quote-box .field.select::after { content: "\25BC"; position: absolute; right: 5px; top: 2px; font-size: 10px; color: #999; }
  .quote-box .btn { position: absolute; left: 77px; top: 154px; width: 96px; height: 16px; border-radius: 8px; background: linear-gradient(#7fc3e6, #3a8dc1);
    color: #fff; font-size: 11px; font-weight: 700; text-align: center; line-height: 16px; }
  .quote-box .note { position: absolute; left: 8px; top: 188px; width: 228px; font-size: 10px; text-align: center; line-height: 12px; }

  .info { top: 602px; width: 244px; height: 112px; }
  .info .bar { height: 26px; color: #fff; font-size: 15px; font-weight: 700; line-height: 26px; padding-left: 20px;
    clip-path: polygon(0 0, 100% 0, 100% 100%, 0 100%, 8px 50%); }
  .info p { font-size: 12px; line-height: 18px; padding: 6px 8px; }
  .info.business { left: 86px; } .info.business .bar { background: linear-gradient(90deg, var(--biz-blue), #6e9cd2); }
  .info.senior { left: 338px; } .info.senior .bar { background: linear-gradient(90deg, var(--car-orange), #e79a6b); }
  .info.contact { left: 588px; } .info.contact .bar { background: linear-gradient(90deg, var(--home-green), #86c27e); }
  .info.senior p { width: 130px; padding-top: 16px; }
  .info.senior .beach { position: absolute; right: 0; top: 26px; width: 110px; height: 84px; background: linear-gradient(to bottom, #cfe6f4, #a8cde0 55%, #e6dcc6); }
  .contact-list { font-size: 12px; line-height: 18px; padding: 5px 0 0 20px; display: grid; grid-template-columns: 52px 1fr; }
  .contact-list dt { text-align: right; padding-right: 8px; }

  .footer-links { left: 86px; top: 733px; font-size: 10.5px; font-weight: 600; line-height: 17px; white-space: nowrap; }
  .badge-plain { top: 725px; height: 36px; }
  .badge-plain.one { left: 664px; width: 87px; background: var(--biz-blue); border-radius: 3px; }
  .badge-plain.two { left: 760px; width: 70px; border: 1px solid var(--panel-border); border-radius: 3px; }
  .badge-plain.two::before { content: ""; position: absolute; left: 4px; top: 4px; width: 26px; height: 26px; border-radius: 50%; border: 3px solid #b0252b; }
  .copyright { left: 126px; top: 781px; font-size: 10px; font-weight: 700; white-space: nowrap; }

  .options-title { left: 914px; top: 150px; font-size: 36px; font-weight: 600; white-space: nowrap; }
  .logo-option { left: 914px; width: 270px; height: 130px; display: flex; align-items: center; font-size: 26px; }
  .logo-option .mark-square { width: 28px; height: 28px; }
</style>
</head>
<body>
  <div class="side-band left"></div>
  <div class="side-band right"></div>

  <header>
    <div class="abs wordmark site-logo"><span class="mark-square"></span>Kvbrimtallow.com</div>
    <p class="abs care">Customer Care: <span>555-014-2290</span></p>
    <ul class="abs util-links"><li>Contacts</li><li>Sitemap</li></ul>
    <ul class="abs main-nav">
      <li class="active">HOME</li><li>AUTO</li><li>LIFE</li><li>HEALTH</li><li>LONG TERM CARE</li>
    </ul>
    <div class="abs nav-rule"></div>
  </header>

  <section class="abs hero life">
    <div class="photo" role="img" aria-label="Photo of a young family holding a baby"></div>
    <h2>LIFE<small>INSURANCE</small></h2>
    <div class="cta">GET A<br>QUOTE</div>
  </section>
  <section class="abs hero car">
    <div class="photo" role="img" aria-label="Photo of a woman waving from a white car"></div>
    <h2>CAR<small>INSURANCE</small></h2>
    <div class="cta">GET A<br>QUOTE</div>
  </section>
  <section class="abs hero home">
    <div class="photo" role="img" aria-label="Photo of a two-storey family house"></div>
    <h2>HOME<small>INSURANCE</small></h2>
    <div class="cta">GET A<br>QUOTE</div>
  </section>

  <section class="abs panel welcome">
    <div class="portrait" role="img" aria-label="Photo of a businessman in a suit holding a briefcase"></div>
    <h1>Welcome At KVBrimtallow,</h1>
    <p>We are dedicated to offering a level of<br>service that will result in lasting relationships<br>with clients. our focus is on helping you find<br>the best possible protection for yourself, your<br>family, or your business at the lowest possible cost.</p>
  </section>

  <section class="abs panel quote-box">
    <h2>Request a Quote<br>Start Saving Today!</h2>
    <label style="left:20px;top:85px;width:44px;">Zip</label>
    <div class="field" style="top:81px;"></div>
    <label style="left:4px;top:115px;width:62px;">Insurance Type</label>
    <div class="field select" style="top:117px;">Auto</div>
    <div class="btn">&#9656; GET QUOTE</div>
    <p class="note">My online quote tool makes it easy for you to request a quote on Auto, Home Owner's/Renter's, Life, Health or Long Term Care insurance.</p>
  </section>

  <section class="abs panel info business">
    <div class="bar">BUSINESS INSURANCE</div>
    <p>If you are interested in business/ commerical or other types of insurance, please contact me by telephone or email to discuss your needs.</p>
  </section>
  <section class="abs panel info senior">
    <div class="bar">OVER 65?</div>
    <p>We have the right insurance for you!</p>
    <div class="beach" role="img" aria-label="Photo of a woman with open arms on a beach"></div>
  </section>
  <section class="abs panel info contact">
    <div class="bar">CONTACT US</div>
    <dl class="contact-list">
      <dt>Phone:</dt><dd>555-014-2290</dd>
      <dt>Email:</dt><dd>anywhere@kvbrimtallow.com</dd>
      <dt>Mail:</dt><dd>1234 Anywhwere Ste<br>Anywhere, AZ, 000000</dd>
    </dl>
  </section>

  <footer>
    <p class="abs footer-links">KVBrimtallow Offers Insurance Quotes on Auto, Home, Health , Life, Business and also Quotes By State.<br>About KVBrimtallow | Contact Us | Member Services | Advertising | Newsletter | Affiliates | Agent Resources</p>
    <div class="abs badge-plain one"></div>
    <div class="abs badge-plain two"></div>
    <p class="abs copyright">Website text Copyright© Kvbrimtallow.com - Auto, Home, Life, Health, Long Term Care Insurance Agent, PHOENIX, AZ, All rights reserved.</p>
  </footer>

  <aside>
    <p class="abs options-title">Logo Options:</p>
    <div class="abs wordmark logo-option" style="top:222px;"><span class="mark-square"></span>Kvbrimtallow.com</div>
    <div class="abs wordmark logo-option" style="top:392px;"><span class="mark-square"></span>Kvbrimtallow.com</div>
    <div class="abs wordmark logo-option" style="top:570px;"><span class="mark-square"></span>Kvbrimtallow.com</div>
  </aside>
</body>
</html>
```